Terra Swift Business Card Design

We need to improve the design of our current business card. We are a erosion control, hydro seeding company that serves many markets. We are attaching the current business card and our logo as reference. You may also visit our site at www.terraswiftllc.example to reference.

```html
<!DOCTYPE html>
<html lang="en">
<head>
<meta charset="utf-8">
<title>Terra Swift Business Card</title>
<link href="https://fonts.googleapis.com/css2?family=Montserrat:wght@400;500;600;800&display=swap" rel="stylesheet">
<style>
  :root {
    --bg: #d9dcdb;
    --white: #ffffff;
    --green-dark: #04532f;
    --green-deep: #033f24;
    --green-bright: #1fa463;
    --green-light: #7fe0ad;
    --ink: #1d1d1d;
  }
  * { margin: 0; padding: 0; box-sizing: border-box; }
  html, body { width: 1200px; height: 1200px; overflow: hidden; background: var(--bg); }
  body { position: relative; font-family: "Montserrat", sans-serif; }

  .card {
    position: absolute;
    left: 150px;
    width: 900px;
    height: 514px;
    border-radius: 34px;
    overflow: hidden;
    box-shadow: 0 10px 26px rgba(0,0,0,0.22);
  }
  .card--front { top: 50px; background: var(--white); }
  .card--back {
    top: 636px;
    background: radial-gradient(ellipse at 45% 40%, #0a6a3e 0%, var(--green-dark) 55%, var(--green-deep) 100%);
  }

  .front-band { position: absolute; left: 0; top: 0; width: 900px; height: 514px; }

  .wordmark {
    position: absolute;
    font-weight: 800;
    color: var(--green-bright);
    white-space: nowrap;
    display: flex;
    align-items: center;
    gap: 12px;
  }
  .wordmark__dot { width: 16px; height: 16px; border-radius: 50%; background: var(--green-bright); flex: none; }
  .card--front .wordmark { left: 60px; top: 262px; font-size: 30px; }
  .card--back .wordmark { left: 0; right: 0; top: 215px; justify-content: center; font-size: 62px; }
  .card--back .wordmark__dot { width: 26px; height: 26px; }

  .contact { position: absolute; left: 505px; top: 78px; color: var(--ink); }
  .contact__name { font-size: 40px; font-weight: 600; color: var(--green-bright); line-height: 1; letter-spacing: -0.5px; }
  .contact__title { font-size: 22px; font-weight: 500; margin: 6px 0 16px; letter-spacing: 0.5px; }
  .contact__list { list-style: none; }
  .contact__item { display: flex; align-items: flex-start; gap: 12px; font-size: 19px; line-height: 1.2; margin-bottom: 9px; }
  .contact__icon { width: 20px; height: 20px; flex: none; margin-top: 2px; fill: var(--green-bright); }

  .website {
    position: absolute;
    right: 48px;
    top: 392px;
    font-size: 22px;
    color: var(--white);
    letter-spacing: 0.3px;
    white-space: nowrap;
  }
  .website__domain { color: var(--green-light); }
</style>
</head>
<body>

<section class="card card--front" aria-label="Card front">
  <svg class="front-band" viewBox="0 0 900 514" aria-hidden="true">
    <path d="M0 470 L410 470 C460 470 470 368 530 368 L900 368 L900 514 L0 514 Z" fill="#1fa463"/>
    <path d="M0 480 L415 480 C465 480 475 378 535 378 L900 378 L900 514 L0 514 Z" fill="#04532f"/>
  </svg>

  <div class="wordmark"><span class="wordmark__dot"></span>Terra Swift Solutions</div>

  <div class="contact">
    <p class="contact__name">FULL NAME</p>
    <p class="contact__title">TITLE</p>
    <ul class="contact__list">
      <li class="contact__item">
        <svg class="contact__icon" viewBox="0 0 24 24"><path d="M6.6 10.8a15.1 15.1 0 0 0 6.6 6.6l2.2-2.2a1 1 0 0 1 1-.25 11.4 11.4 0 0 0 3.6.57 1 1 0 0 1 1 1V20a1 1 0 0 1-1 1A17 17 0 0 1 3 4a1 1 0 0 1 1-1h3.5a1 1 0 0 1 1 1 11.4 11.4 0 0 0 .57 3.6 1 1 0 0 1-.25 1z"/></svg>
        (555) 014-2210
      </li>
      <li class="contact__item">
        <svg class="contact__icon" viewBox="0 0 24 24"><path d="M7 2h10v5H7zM3 8h18v11h-4v3H7v-3H3zm6 9v3h6v-3zm8-6a1 1 0 1 0 0 2 1 1 0 0 0 0-2z"/></svg>
        (555) 014-2211
      </li>
      <li class="contact__item">
        <svg class="contact__icon" viewBox="0 0 24 24"><path d="M2 5h20v14H2zm2 2v.5l8 5 8-5V7l-8 5z"/></svg>
        info@terraswiftllc.example
      </li>
      <li class="contact__item">
        <svg class="contact__icon" viewBox="0 0 24 24"><path d="M12 2a7 7 0 0 0-7 7c0 5 7 13 7 13s7-8 7-13a7 7 0 0 0-7-7zm0 9.5A2.5 2.5 0 1 1 12 6.5a2.5 2.5 0 0 1 0 5z"/></svg>
        <span>72 Fernbrook Road<br>Millbrook, NC 28000</span>
      </li>
    </ul>
  </div>

  <p class="website">www.<span class="website__domain">terraswiftllc.example</span></p>
</section>

<section class="card card--back" aria-label="Card back">
  <div class="wordmark"><span class="wordmark__dot"></span>Terra Swift Solutions</div>
</section>

</body>
</html>
```